Vorna Fleet business card

I am needing a business card that at a glance shows all the services that we provide emphasizing some more than others. We are a Fleet and Compliance management company as well as a software company. We provide outsourced solutions for KPX compliance and HR services via our own software.
In addition, we do
drug testing
GPS
Cameras
Electronic DVIRS
ELD's

Target Market(s)

Transportation company owners

Industry/Entity Type

Transportation supplier

Contact Information for Business Card

the card should inform potential customers what we do

Other font styles liked:
• I have added brand guidelines. See attached

Requirements
Must have
• See description
Should not have
• Colors outside my brand guide. See attached

```html
<!DOCTYPE html>
<html lang="en">
<head>
<meta charset="UTF-8">
<title>Vorna Fleet Business Card</title>
<link href="https://fonts.googleapis.com/css2?family=Open+Sans:ital,wght@0,400;0,600;0,800;1,400&display=swap" rel="stylesheet">
<style>
  :root {
    --stage: #2a2a2a;
    --card: #1d1d1d;
    --card-back: #191919;
    --red: #e3262d;
    --white: #f4f4f4;
    --muted: #3a3a3a;
  }
  * { margin: 0; padding: 0; box-sizing: border-box; }
  html, body { width: 1200px; height: 900px; overflow: hidden; }
  body {
    background: var(--stage);
    font-family: "Open Sans", Arial, sans-serif;
    display: flex;
    flex-direction: column;
    align-items: center;
    justify-content: center;
    gap: 36px;
  }
  .card {
    position: relative;
    width: 700px;
    height: 400px;
    background: var(--card);
    border-bottom: 8px solid var(--red);
    box-shadow: 0 12px 30px rgba(0,0,0,.45);
  }
  .card--front { display: flex; }
  .brand {
    position: absolute;
    left: 70px;
    top: 120px;
    width: 300px;
    display: flex;
    align-items: center;
    gap: 14px;
    color: var(--white);
    font-weight: 800;
    font-size: 42px;
    letter-spacing: 1px;
  }
  .brand__mark { width: 22px; height: 22px; background: var(--red); flex: none; }
  .divider {
    position: absolute;
    left: 395px;
    top: 70px;
    width: 1px;
    height: 200px;
    background: var(--red);
  }
  .contact {
    position: absolute;
    left: 425px;
    top: 90px;
    color: var(--white);
  }
  .contact__name {
    color: var(--red);
    font-weight: 800;
    font-size: 24px;
    text-transform: uppercase;
    letter-spacing: .5px;
  }
  .contact__title { font-size: 17px; margin-bottom: 22px; }
  .contact__list { list-style: none; font-size: 17px; line-height: 1.7; }
  .contact__list li { display: flex; align-items: center; gap: 10px; }
  .contact__list svg { width: 14px; height: 14px; fill: var(--red); flex: none; }
  .services {
    position: absolute;
    left: 0; right: 0;
    bottom: 34px;
    text-align: center;
    color: var(--white);
    font-size: 17px;
  }
  .services .dot { color: var(--red); margin: 0 8px; }
  .card--back {
    background: var(--card-back);
    display: flex;
    align-items: center;
    justify-content: center;
  }
  .brand--faint {
    font-weight: 800;
    font-size: 64px;
    color: var(--muted);
    letter-spacing: 2px;
  }
</style>
</head>
<body>
  <section class="card card--front">
    <div class="brand"><span class="brand__mark"></span>Vorna Fleet</div>
    <div class="divider"></div>
    <div class="contact">
      <div class="contact__name">Dana Kessler</div>
      <div class="contact__title">President</div>
      <ul class="contact__list">
        <li><svg viewBox="0 0 24 24"><path d="M6.6 10.8a15 15 0 0 0 6.6 6.6l2.2-2.2a1 1 0 0 1 1-.25 11.4 11.4 0 0 0 3.6.57 1 1 0 0 1 1 1V20a1 1 0 0 1-1 1A17 17 0 0 1 3 4a1 1 0 0 1 1-1h3.5a1 1 0 0 1 1 1c0 1.25.2 2.45.57 3.6a1 1 0 0 1-.25 1z"/></svg>555-014-2287</li>
        <li><svg viewBox="0 0 24 24"><path d="M2 5h20v14H2z M2 5l10 8 10-8" /></svg>info@vornafleet.com</li>
        <li><svg viewBox="0 0 24 24"><circle cx="12" cy="12" r="10"/></svg>www.vornafleet.com</li>
      </ul>
    </div>
    <p class="services">Drug Testing<span class="dot">•</span>GPS<span class="dot">•</span>Cameras<span class="dot">•</span>Electronic DVIRS<span class="dot">•</span>ELD's</p>
  </section>

  <section class="card card--back">
    <div class="brand--faint">Vorna Fleet</div>
  </section>
</body>
</html>
```